TRAVEX CONSULTING / PROJECT MANAGEMENT WEB DESIGN

Design Brief: Travex Consulting Website

I own 'TRAVEX' business name and therefore can keep the name and logo simple i.e. TRAVEX only and incorporate consulting / Project Management within the design or text.

Purpose:

The purpose of this project is to create a website for Travex.com.au, a project management consulting company. The website will promote the company's services, allowing potential clients to learn more about Travex and its capabilities. The website should be professional, easy to navigate, and provide all necessary information for potential clients.

Target Audience:

Clients in the Oil & Gas, LNG, and Chemical industry
Businesses and organizations in need of project management and engineering consultancy services
Potential clients looking for information about the company and its services
Key Elements:
Clean and modern design that reflects the company's professional image and incorporates the company logo

Clear and easy-to-use navigation menu

“Homepage” that promotes the company's main services and includes the company's mission statement.

Services:

PROJECT MANAGEMENT
PROJECT ENGINEERING
QUALITY MANAGEMENT AND PROCESS DEVELOPMENT
BUSINESS CASE DEVELOPMENT
ENGINEERING & DESIGN MANAGEMENT
CONCEPT STUDIES AND PROJECT SUPPORT
CONSTRUCTION MANAGEMENT
CONTRACT MANAGEMENT / CLAIMS PROCUREMENT / SUPPLY CHAIN SUPPORT
COMMERCIAL LIABILITY & RISK MANAGEMENT

Mission Statement:

"Our mission at Travex is to provide expert project management and engineering consultancy services that help our clients achieve their goals and exceed their expectations. We will accomplish this by offering a full range of services, providing experienced and highly-qualified professionals, building strong relationships with our clients, continuously improving our services, and maintaining a reputation for excellence."

"About" page that includes client-supplied text about the company
"Contact" page with an editable form, email, and phone number for potential clients to get in touch with the company

Design Style:

Professional and modern
Clean and simple layout
Use of the company's colors and branding (subject to change)
Use of high-quality images that reflect the industry and services

Functionality:
Responsive design that is optimized for all devices and screen sizes

Website will be coded and uploaded to a content management system (CMS) for easy updates and maintenance
Website will be optimized for search engines and include all necessary SEO elements
Website will be fully tested for compatibility with all modern web browsers and devices
Website will be secured with an SSL certificate to ensure the safety of user data (client hosting includes SSL certificate).

Target Market(s)

Clients in the Oil & Gas, LNG, and Chemical industry Businesses and organizations in need of project management and engineering consultancy services Potential clients looking for information about the company and its services

Industry/Entity Type

Oil & Gas, LNG, and Chemical industry Businesses and organizations

Coding

Coded - Design and coding required

Number of Pages Required

3 page

Font styles to use
Sans Serif

Colors
0054AA
0677BA
7BADD7
CADEEF
E8F1F8
EB3D1F
EC4F4E
F09395
F8D3D4
FCEDEE
6B429C
8869AF
B7A5CE
E3DAEB
F3F0F8

Requirements
Must have
• HOME ABOUT AND CONTACT PAGE
Nice to have
• Fresh look, open to ideas
Should not have
• Stock images and hand shakes and meeting rooms..

```html
<!DOCTYPE html>
<html lang="en">
<head>
<meta charset="utf-8">
<title>Travex Resources – Project Management and Engineering Consultancy</title>
<link href="https://fonts.googleapis.com/css2?family=Raleway:wght@300;400;500;600;700;800&display=swap" rel="stylesheet">
<style>
:root{
  --blue:#2aa6f4;
  --blue-deep:#1a8de0;
  --ink:#2c3040;
  --text:#3a3d48;
  --muted:#6d7180;
  --pale:#eef3f9;
  --field:#f3f4f6;
  --white:#ffffff;
}
*{box-sizing:border-box;margin:0;padding:0}
html,body{width:1200px;height:4019px;overflow:hidden}
body{position:relative;font-family:"Raleway",sans-serif;color:var(--text);background:var(--white)}
.abs{position:absolute}
a{color:inherit;text-decoration:none}

/* header */
.topbar{left:400px;top:0;width:631px;height:31px;background:var(--ink);border-bottom-left-radius:22px;color:#fff;font-size:10px;font-weight:600}
.topbar .phone{left:132px;top:10px}
.topbar .mail{left:249px;top:10px}
.topbar svg{vertical-align:-2px;margin-right:5px}
.search{left:382px;top:3px;width:248px;height:25px;background:#3a3e4f;color:#a8acb8;font-size:9px;padding:7px 14px}
.search svg{position:absolute;right:10px;top:7px}
.brand{left:169px;top:38px;font-weight:700;font-size:16px;color:var(--blue);letter-spacing:.2px;display:flex;align-items:center;gap:8px}
.brand .dot{width:22px;height:22px;border-radius:50%;background:var(--blue)}
.nav{top:60px;font-size:12px;font-weight:600;color:var(--ink)}
.btn-start{left:911px;top:50px;width:120px;height:34px;border-radius:17px;background:var(--blue);color:#fff;font-size:12px;font-weight:600;display:flex;align-items:center;justify-content:center}

/* hero */
.hero-photo{left:0;top:100px;width:1200px;height:620px;background:linear-gradient(100deg,#3c5a86 0%,#6f8db0 24%,#b8cde0 44%,#dfe8f1 62%,#cfdbe7 80%,#a9b8c6 100%)}
.hero-title{left:557px;top:166px;color:var(--ink);line-height:38px}
.hero-title .b{display:block;font-weight:800;font-size:33px;letter-spacing:-.2px}
.hero-title .l{display:block;font-weight:300;font-size:33px}
.hero-copy{left:557px;top:256px;width:460px;font-size:10.5px;line-height:19px;color:var(--text)}
.btn-dark{background:var(--ink);color:#fff;font-size:11px;font-weight:600;border-radius:18px;display:flex;align-items:center;justify-content:center}
.hero-btn{left:557px;top:332px;width:137px;height:33px}
.hero-curve{left:0;top:540px}

/* section headings */
.heading{font-size:29px;color:var(--ink);font-weight:300;letter-spacing:.3px}
.heading strong{font-weight:800}
.services-head{left:0;width:1200px;top:712px;text-align:center}

/* services */
.service{width:268px;text-align:center}
.service .disc{width:268px;height:205px;overflow:hidden;position:relative}
.service .photo{width:268px;height:268px;border-radius:50%}
.service .disc svg{position:absolute;left:0;top:0}
.service h3{margin-top:18px;font-size:14px;font-weight:700;color:var(--ink);line-height:18px;letter-spacing:.4px}
.g1{background:linear-gradient(135deg,#e7ecf2,#8b9aae)}
.g2{background:linear-gradient(135deg,#f1f2f4,#b9bec6)}
.g3{background:linear-gradient(135deg,#b8d0e6,#4f6d87)}
.g4{background:linear-gradient(135deg,#c7ccd4,#6e7d91)}
.g5{background:linear-gradient(135deg,#eeeeee,#9fa6b0)}
.g6{background:linear-gradient(135deg,#d9d5cd,#7a7f88)}
.g7{background:linear-gradient(135deg,#b7b1a3,#4e5a66)}
.g8{background:linear-gradient(135deg,#2d4a63,#101d2b)}
.g9{background:linear-gradient(135deg,#7c5638,#d6b693)}

/* mission */
.mission{left:0;top:1726px;width:1200px;height:480px;background:var(--pale)}
.mission-head{left:114px;top:1804px}
.mission-copy{left:155px;top:1866px;width:380px;font-size:12px;line-height:25px;color:var(--text)}
.mission-copy p+p{margin-top:25px}
.mission-btn{left:155px;top:2091px;width:140px;height:34px}
.mission-photo{left:600px;top:1726px}

/* about */
.about-ring{left:115px;top:2284px;width:380px;height:380px;border-radius:50%;border:1.5px solid #d9dde3}
.about-photo{left:150px;top:2281px;width:412px;height:412px;border-radius:50%;background:linear-gradient(140deg,#6f7f93 0%,#c2c9d2 45%,#e6e9ec 70%,#9aa6b3 100%)}
.about-head{left:641px;top:2314px}
.about-copy{left:645px;top:2378px;width:410px;font-size:12px;line-height:25px}
.about-copy p+p{margin-top:25px}
.about-btn{left:645px;top:2628px;width:140px;height:33px}

/* contact */
.touch{left:0;top:2779px;width:1200px;height:640px;background:var(--pale)}
.touch-head{left:0;width:1200px;top:2836px;text-align:center}
.footer-bg{left:0;top:3420px;width:1200px;height:599px;background:var(--ink)}
.touch-curve{left:0;top:3330px}
.card{left:158px;top:2923px;width:883px;height:467px;background:#fff;box-shadow:0 18px 30px rgba(40,50,70,.10)}
.card-title{left:78px;top:70px;font-size:22px;font-weight:700;color:#111}
.card-sub{left:80px;top:103px;width:240px;font-size:10px;line-height:16px;color:var(--text)}
.info{left:78px;display:flex;gap:14px}
.info .ic{width:52px;height:52px;border-radius:50%;background:#e6f3fd;display:flex;align-items:center;justify-content:center}
.info .ic span{width:38px;height:38px;border-radius:50%;background:var(--blue);display:flex;align-items:center;justify-content:center}
.info h4{font-size:14px;font-weight:700;color:#111;margin-top:6px}
.info p{font-size:9.5px;line-height:15px;width:200px;margin-top:2px}
.field{left:429px;width:371px;background:var(--field);border:1px solid #e6e8eb;font-size:9.5px;color:#7a7e88;padding:0 0 0 20px;display:flex;align-items:center;gap:12px}
.field.active{color:#26a36b}
.field.active .caret{width:1px;height:16px;background:#555;margin-left:14px}
.field.msg{align-items:flex-start;padding-top:16px}
.submit{left:429px;top:374px;width:371px;height:42px;background:var(--ink);color:#fff;font-size:11px;font-weight:700;letter-spacing:.4px}
.submit span{position:absolute;left:0;width:302px;top:14px;text-align:center}
.submit i{position:absolute;right:0;top:0;width:69px;height:42px;background:var(--blue);display:flex;align-items:center;justify-content:center}

/* footer */
.foot-brand{left:169px;top:3670px;font-size:13px}
.foot-brand .dot{width:18px;height:18px}
.foot-about{left:169px;top:3710px;width:190px;font-size:9.5px;line-height:16px;color:#dfe2ea}
.foot-col h5{font-size:12.5px;font-weight:700;color:#fff;padding-bottom:5px;border-bottom:1.5px solid var(--blue);display:inline-block}
.foot-list{font-size:9.5px;color:#dfe2ea;line-height:15px}
.foot-list li{list-style:none;margin-bottom:15px}
.copy{left:169px;top:3980px;font-size:9.5px;color:#dfe2ea}
.terms{left:932px;top:3980px;font-size:9.5px;color:#dfe2ea}
</style>
</head>
<body>

<!-- header -->
<div class="abs topbar">
  <div class="abs phone"><svg width="10" height="10" viewBox="0 0 24 24" fill="#2aa6f4"><path d="M6.6 10.8a15 15 0 0 0 6.6 6.6l2.2-2.2c.3-.3.7-.4 1-.2 1.1.4 2.3.6 3.6.6.6 0 1 .4 1 1V20c0 .6-.4 1-1 1A17 17 0 0 1 3 4c0-.6.4-1 1-1h3.5c.6 0 1 .4 1 1 0 1.3.2 2.5.6 3.6.1.3 0 .7-.2 1z"/></svg>020-555-01-234</div>
  <div class="abs mail"><svg width="11" height="9" viewBox="0 0 24 18" fill="#2aa6f4"><path d="M0 0h24v18H0z M2 2l10 7 10-7" stroke="#2c3040" stroke-width="2"/></svg>info@Travex.com</div>
  <div class="abs search">Search...<svg width="11" height="11" viewBox="0 0 24 24" fill="none" stroke="#8d92a0" stroke-width="2.5"><circle cx="10" cy="10" r="7"/><path d="M15 15l6 6"/></svg></div>
</div>
<div class="abs brand"><span class="dot"></span>TRAVEX RESOURCES</div>
<a class="abs nav" style="left:661px">Home</a>
<a class="abs nav" style="left:733px">About</a>
<a class="abs nav" style="left:807px">Contact Us</a>
<a class="abs btn-start">Get Started</a>

<!-- hero -->
<div class="abs hero-photo" role="img" aria-label="Two engineers in hard hats on a refinery walkway overlooking an industrial plant"></div>
<h1 class="abs hero-title"><span class="b">PROJECT MANAGEMENT AND</span><span class="l">ENGINEERING CONSULTANCY</span></h1>
<p class="abs hero-copy">Lorem ipsum dolor sit amet, consectetur adipisicing elit, sed do eiusmod tempor incididunt ut labore et dolore magna aliqua. Ut enim ad minim veniam, quis nostrud exercitation ullamco laboris nisi ut aliquip ex ea commodo consequat.</p>
<a class="abs btn-dark hero-btn">Request Services</a>
<svg class="abs hero-curve" width="1200" height="260" viewBox="0 0 1200 260" aria-hidden="true">
  <path d="M0 235 C260 70 650 15 1200 130 L1200 260 L0 260Z" fill="#2aa6f4"/>
  <path d="M0 260 L0 250 C330 90 720 70 1200 160 L1200 260Z" fill="#fff"/>
</svg>

<!-- services -->
<h2 class="abs heading services-head">OUR <strong>SERVICES</strong></h2>

<svg width="0" height="0" style="position:absolute" aria-hidden="true">
  <defs>
    <symbol id="disc-wave" viewBox="0 0 268 205">
      <path d="M0 205 L0 180 C60 135 150 125 268 165 L268 205Z" fill="#2aa6f4"/>
      <path d="M0 205 L0 200 C70 160 165 155 268 192 L268 205Z" fill="#fff"/>
    </symbol>
  </defs>
</svg>

<div class="abs service" style="left:156px;top:813px"><div class="disc" role="img" aria-label="Consultant reviewing a project plan on a whiteboard"><div class="photo g1"></div><svg width="268" height="205" aria-hidden="true"><use href="#disc-wave"/></svg></div><h3>PROJECT<br>MANAGEMENT</h3></div>
<div class="abs service" style="left:462px;top:813px"><div class="disc" role="img" aria-label="Engineers marking up technical drawings"><div class="photo g2"></div><svg width="268" height="205" aria-hidden="true"><use href="#disc-wave"/></svg></div><h3>PROJECT<br>ENGINEERING</h3></div>
<div class="abs service" style="left:766px;top:813px"><div class="disc" role="img" aria-label="Inspector with a tablet on a factory floor"><div class="photo g3"></div><svg width="268" height="205" aria-hidden="true"><use href="#disc-wave"/></svg></div><h3>QUALITY MANAGEMENT<br>AND PROCESS DEVELOPMENT</h3></div>

<div class="abs service" style="left:156px;top:1105px"><div class="disc" role="img" aria-label="Hands pointing at charts on a tablet"><div class="photo g4"></div><svg width="268" height="205" aria-hidden="true"><use href="#disc-wave"/></svg></div><h3>BUSINESS<br>CASE DEVELOPMENT</h3></div>
<div class="abs service" style="left:462px;top:1105px"><div class="disc" role="img" aria-label="Design plans being reviewed on a desk"><div class="photo g5"></div><svg width="268" height="205" aria-hidden="true"><use href="#disc-wave"/></svg></div><h3>ENGINEERING &amp; DESIGN<br>MANAGEMENT</h3></div>
<div class="abs service" style="left:766px;top:1105px"><div class="disc" role="img" aria-label="Team discussing concept studies around a laptop"><div class="photo g6"></div><svg width="268" height="205" aria-hidden="true"><use href="#disc-wave"/></svg></div><h3>CONCEPT STUDIES AND<br>PROJECT SUPPORT</h3></div>

<div class="abs service" style="left:156px;top:1397px"><div class="disc" role="img" aria-label="Construction crew in hard hats around site plans"><div class="photo g7"></div><svg width="268" height="205" aria-hidden="true"><use href="#disc-wave"/></svg></div><h3>CONSTRUCTION<br>MANAGEMENT</h3></div>
<div class="abs service" style="left:462px;top:1397px"><div class="disc" role="img" aria-label="Technician with a laptop in a server room"><div class="photo g8"></div><svg width="268" height="205" aria-hidden="true"><use href="#disc-wave"/></svg></div><h3>SUPPLY CHAIN<br>SUPPORT</h3></div>
<div class="abs service" style="left:766px;top:1397px"><div class="disc" role="img" aria-label="Hand stopping a row of falling wooden blocks"><div class="photo g9"></div><svg width="268" height="205" aria-hidden="true"><use href="#disc-wave"/></svg></div><h3>COMMERCIAL LIABILITY &amp;<br>RISK MANAGEMENT</h3></div>

<!-- mission -->
<section class="abs mission"></section>
<h2 class="abs heading mission-head"><strong>MISSION</strong> STATEMENT</h2>
<div class="abs mission-copy">
  <p>"Our mission at Travex is to provide expert project management and engineering consultancy services that help our clients achieve their goals and exceed their expectations.</p>
  <p>We will accomplish this by offering a full range of services, providing experienced and highly-qualified professionals, building strong relationships with our clients, continuously improving our services, and maintaining a reputation for excellence."</p>
</div>
<a class="abs btn-dark mission-btn">Lear More</a>
<svg class="abs mission-photo" width="600" height="480" viewBox="0 0 600 480" role="img" aria-label="LNG storage spheres at a waterfront terminal under a blue sky">
  <defs>
    <linearGradient id="lng" x1="0" y1="0" x2="0" y2="1">
      <stop offset="0" stop-color="#1f6fc8"/>
      <stop offset=".45" stop-color="#9cc3e6"/>
      <stop offset=".62" stop-color="#d9dfe4"/>
      <stop offset=".78" stop-color="#3a6f97"/>
      <stop offset="1" stop-color="#1b4d78"/>
    </linearGradient>
  </defs>
  <path d="M150 0 C20 90 -20 330 55 480 L600 480 L600 0Z" fill="#2aa6f4"/>
  <path d="M190 0 C60 100 40 330 90 480 L600 480 L600 0Z" fill="url(#lng)"/>
</svg>

<!-- about -->
<div class="abs about-ring"></div>
<div class="abs about-photo" role="img" aria-label="Two engineers in hard hats studying a blueprint"></div>
<h2 class="abs heading about-head"><strong>ABOUT TRAVEX</strong> CONSULTING</h2>
<div class="abs about-copy">
  <p>Lorem ipsum dolor sit amet, consectetur adipisicing elit, sed do eiusmod tempor incididunt ut labore et dolore magna aliqua. Ut enim ad minim veniam, quis nostrud exercitation ullamco laboris nisi ut aliquip ex ea commodo consequat.</p>
  <p>Duis aute irure dolor in reprehenderit in voluptate velit esse cillum dolore eu fugiat nulla pariatur. Excepteur sint occaecat cupidatat non proident, sunt in culpa qui officia deserunt mollit anim id est laborum. Sed ut perspiciatis unde omnis iste natus error sit voluptatem.</p>
</div>
<a class="abs btn-dark about-btn">Lear More</a>

<!-- contact -->
<section class="abs touch"></section>
<div class="abs footer-bg"></div>
<svg class="abs touch-curve" width="1200" height="260" viewBox="0 0 1200 260" aria-hidden="true">
  <path d="M0 0 H1200 V80 C850 230 380 230 0 60Z" fill="#eef3f9"/>
  <path d="M0 60 C380 230 850 230 1200 80 L1200 100 C860 290 380 300 0 130Z" fill="#2aa6f4"/>
  <path d="M0 130 C380 300 860 290 1200 100 L1200 260 L0 260Z" fill="#2c3040"/>
</svg>
<h2 class="abs heading touch-head"><strong>GET IN</strong> TOUCH</h2>

<div class="abs card">
  <h3 class="abs card-title">Contact Us</h3>
  <p class="abs card-sub">Learn better and faster from the world's best company with the newest.</p>

  <div class="abs info" style="top:164px">
    <div class="ic"><span><svg width="18" height="18" viewBox="0 0 24 24" fill="none" stroke="#fff" stroke-width="2"><path d="M12 22s7-7 7-12a7 7 0 0 0-14 0c0 5 7 12 7 12z"/><circle cx="12" cy="10" r="2.5"/></svg></span></div>
    <div><h4>Location:</h4><p>Lorem ipsum dolor sit amet, consectetur adipisicing elit, sed</p></div>
  </div>
  <div class="abs info" style="top:253px">
    <div class="ic"><span><svg width="18" height="18" viewBox="0 0 24 24" fill="none" stroke="#fff" stroke-width="2"><rect x="3" y="5" width="18" height="14"/><path d="M3 6l9 7 9-7"/></svg></span></div>
    <div><h4>Email Address:</h4></div>
  </div>
  <div class="abs info" style="top:339px">
    <div class="ic"><span><svg width="18" height="18" viewBox="0 0 24 24" fill="#fff"><path d="M6.6 10.8a15 15 0 0 0 6.6 6.6l2.2-2.2c.3-.3.7-.4 1-.2 1.1.4 2.3.6 3.6.6.6 0 1 .4 1 1V20c0 .6-.4 1-1 1A17 17 0 0 1 3 4c0-.6.4-1 1-1h3.5c.6 0 1 .4 1 1 0 1.3.2 2.5.6 3.6.1.3 0 .7-.2 1z"/></svg></span></div>
    <div><h4>Phone Number:</h4><p>020-555-01-234</p></div>
  </div>

  <div class="abs field active" style="top:47px;height:45px"><svg width="12" height="12" viewBox="0 0 24 24" fill="none" stroke="#26a36b" stroke-width="2"><circle cx="12" cy="8" r="4"/><path d="M4 21c1-5 15-5 16 0"/></svg>Jonathan Doe<span class="caret"></span></div>
  <div class="abs field" style="top:104px;height:44px"><svg width="10" height="13" viewBox="0 0 16 24" fill="none" stroke="#7a7e88" stroke-width="2"><rect x="2" y="2" width="12" height="20" rx="2"/></svg>Phone No</div>
  <div class="abs field" style="top:161px;height:45px"><svg width="13" height="10" viewBox="0 0 24 18" fill="none" stroke="#7a7e88" stroke-width="2"><rect x="1" y="1" width="22" height="16"/><path d="M1 2l11 8 11-8"/></svg>Email Address</div>
  <div class="abs field msg" style="top:220px;height:132px"><svg width="13" height="12" viewBox="0 0 24 22" fill="none" stroke="#7a7e88" stroke-width="2"><path d="M2 3h20v12H9l-5 4v-4H2z"/></svg>Message</div>
  <div class="abs submit"><span>SUBMITT NOW</span><i><svg width="22" height="20" viewBox="0 0 24 22" fill="#fff"><path d="M0 10 L24 0 L18 22 L11 14 L20 4 L8 12Z"/></svg></i></div>
</div>

<!-- footer -->
<div class="abs brand foot-brand"><span class="dot"></span>TRAVEX RESOURCES</div>
<p class="abs foot-about">Lorem ipsum dolor sit amet, consectetur adipisicing elit, sed do eiusmod tempor incididunt ut labore et dolore.</p>

<div class="abs foot-col" style="left:443px;top:3676px"><h5>Quick Links</h5></div>
<ul class="abs foot-list" style="left:445px;top:3731px">
  <li>Home</li><li>About</li><li>Services</li><li>Contact Us</li>
</ul>

<div class="abs foot-col" style="left:627px;top:3676px"><h5>Services</h5></div>
<ul class="abs foot-list" style="left:628px;top:3731px;width:170px">
  <li>Project Management</li>
  <li>Project Engineering</li>
  <li>Quality Management And Process Development</li>
  <li>Business Case Development</li>
  <li>Engineering &amp; Design Management</li>
</ul>
<ul class="abs foot-list" style="left:825px;top:3731px;width:210px">
  <li>Concept Studies And Project Support</li>
  <li>Construction Management</li>
  <li>Contract Management / Claims Procurement / Supply Chain Support</li>
  <li>Commercial Liability &amp; Risk Management</li>
</ul>

<p class="abs copy">Copyright © 2023 Travex Resources. All Rights Reserved.</p>
<p class="abs terms">Terms &amp; Privacy Policy</p>

</body>
</html>
```